The Kelbridge Dog Stylist

I have a logo which I designed myself ( I tried a contest and it did not work out well..not on this site) The logo needs some tweaking for example "THE" needs to be put above "KELBRIDGE" in line with the D (on top)and it needs to be going across sideways.Also the dog is not exactly in the middle.
Also on the card I would like my name written in a simple running writing script
Margot

Then in plain writing:
17B Harlow St Tarrowin NSW 2871
Ph. 6391 5073
On the back:
Your next appointment:
...........................................

Pet bathing, clipping and styling

• The logo going across lengthways and changed a bit (as explained above)

```html
<!DOCTYPE html>
<html lang="en">
<head>
<meta charset="utf-8">
<title>The Kelbridge Dog Stylist – Business Card</title>
<link rel="stylesheet" href="https://fonts.googleapis.com/css2?family=Anton&family=Great+Vibes&family=Open+Sans:wght@600&family=Fira+Sans+Condensed:ital,wght@0,400;1,600&display=swap">
<style>
  :root {
    --brand-red: #e8141b;
    --ink: #111111;
    --paper: #ffffff;
    --page: #ffffff;
    --shadow: #3c3c3c;
    --paw-grey: #b9b9b9;
    --paw-black: #0a0a0a;
  }
  * { box-sizing: border-box; margin: 0; padding: 0; }
  html, body {
    width: 1200px;
    height: 605px;
    overflow: hidden;
    background: var(--page);
  }
  .canvas {
    position: relative;
    width: 1200px;
    height: 605px;
  }
  .card {
    position: absolute;
    width: 555px;
    height: 330px;
    background: var(--paper);
    box-shadow: 8px 8px 5px var(--shadow);
  }
  .card__band {
    position: absolute;
    left: 0; top: 0;
    width: 100%;
    height: 12px;
    background: var(--brand-red);
  }
  .card--front { left: 35px; top: 42px; }
  .card--back  { left: 612px; top: 217px; border-left: 1px solid #cfcfcf; }

  /* Front */
  .brand-name {
    position: absolute;
    left: 22px;
    top: 150px;
    width: 250px;
    font-family: "Anton", sans-serif;
    font-weight: 400;
    font-size: 44px;
    line-height: 1.05;
    text-transform: uppercase;
    color: var(--brand-red);
  }
  .owner-name {
    position: absolute;
    left: 258px;
    top: 30px;
    font-family: "Great Vibes", cursive;
    font-size: 50px;
    line-height: 1;
    color: var(--brand-red);
  }
  .contact {
    position: absolute;
    left: 258px;
    top: 81px;
    font-family: "Open Sans", sans-serif;
    font-style: normal;
    font-weight: 600;
    font-size: 18px;
    line-height: 26px;
    color: var(--ink);
    white-space: nowrap;
  }
  .paw {
    position: absolute;
    width: 88px;
    height: 88px;
    border-radius: 44% 44% 40% 40%;
  }
  .paw--grey { background: var(--paw-grey); }
  .paw--black { background: var(--paw-black); }
  .card--front .paw--one { left: 342px; top: 210px; }
  .card--front .paw--two { left: 450px; top: 200px; }

  /* Back */
  .appointment-label {
    position: absolute;
    left: 50px;
    top: 56px;
    font-family: "Fira Sans Condensed", sans-serif;
    font-weight: 400;
    font-size: 18px;
    color: var(--brand-red);
  }
  .appointment-line {
    position: absolute;
    left: 50px;
    top: 94px;
    width: 202px;
    border-top: 2px dotted var(--brand-red);
  }
  .services {
    position: absolute;
    left: 50px;
    top: 130px;
    font-family: "Fira Sans Condensed", sans-serif;
    font-style: italic;
    font-weight: 600;
    font-size: 20px;
    color: var(--brand-red);
  }
  .card--back .paw--one { left: 308px; top: 205px; }
  .card--back .paw--two { left: 418px; top: 195px; }
</style>
</head>
<body>
<main class="canvas">

  <section class="card card--front" aria-label="Card front">
    <div class="card__band"></div>
    <p class="brand-name">The Kelbridge Dog Stylist</p>
    <p class="owner-name">Margot</p>
    <address class="contact">
      17B Harlow St Tarrowin NSW 2871<br>
      Ph. 6391 5073
    </address>
    <div class="paw paw--grey paw--one" role="img" aria-label="Grey paw print"></div>
    <div class="paw paw--grey paw--two" role="img" aria-label="Grey paw print"></div>
  </section>

  <section class="card card--back" aria-label="Card back">
    <div class="card__band"></div>
    <p class="appointment-label">Your next appointment:</p>
    <div class="appointment-line"></div>
    <p class="services">Pet bathing, clipping and styling</p>
    <div class="paw paw--black paw--one" role="img" aria-label="Black paw print"></div>
    <div class="paw paw--black paw--two" role="img" aria-label="Black paw print"></div>
  </section>

</main>
</body>
</html>
```